Tovimerra: Travel business card redesign

We need a clean elegant look for our cards featuring blue and orange. Look should communicate a sense of strong design and seem uncluttered. The company is Tovimerra which means drift into calm. As in every trip is an drift into calm. Feel free to reinvent the logo or just tweak it. Colors should be blue like Caribbean waters and a saturated orange. Keep it clean and simple.
Please match the information in the sample uploaded but the sample is horrible -- a non-starter -- use for information only. also please add managing director to my name as title

Target Market(s)
potential clients, hotels, trade publications
Industry/Entity Type
Travel Industry
Contact Information for Business Card
as above
Requirements
Must have
- Font should be century gothic. Colors below are close but a but prefer lighter in each case.

```html
<!DOCTYPE html>
<html lang="en">
<head>
<meta charset="utf-8">
<title>Tovimerra – Business Card</title>
<link href="https://fonts.googleapis.com/css2?family=Questrial&display=swap" rel="stylesheet">
<style>
  :root {
    --backdrop: #cfcfd1;
    --card-white: #ffffff;
    --lagoon: #8db6dc;
    --lagoon-light: #a9c9e6;
    --orange: #d9832b;
    --ink-white: #ffffff;
  }
  * { margin: 0; padding: 0; box-sizing: border-box; }
  html, body {
    width: 1200px;
    height: 809px;
    overflow: hidden;
  }
  body {
    background: var(--backdrop);
    font-family: "Questrial", "Century Gothic", sans-serif;
    position: relative;
  }
  .card {
    position: absolute;
    top: 120px;
    width: 320px;
    height: 560px;
    overflow: hidden;
    box-shadow: 0 10px 28px rgba(0, 0, 0, 0.18);
  }
  .card--front { left: 250px; background: var(--card-white); }
  .card--back {
    left: 630px;
    background: linear-gradient(160deg, var(--lagoon-light), var(--lagoon));
  }

  /* Front */
  .brand {
    position: absolute;
    top: 130px;
    left: 28px;
    right: 24px;
    display: flex;
    align-items: flex-start;
    gap: 8px;
  }
  .brand__name {
    color: var(--orange);
    font-size: 38px;
    line-height: 1;
  }
  .brand__tagline {
    color: var(--lagoon);
    font-size: 12px;
    line-height: 1;
    margin-top: 2px;
    white-space: nowrap;
  }
  .person {
    position: absolute;
    left: 28px;
    top: 372px;
    color: var(--orange);
  }
  .person__name { font-size: 17px; font-weight: 700; }
  .person__title { font-size: 15px; margin-top: 2px; }
  .contact-band {
    position: absolute;
    left: 0;
    right: 0;
    bottom: 0;
    height: 150px;
    background: var(--lagoon);
    padding: 22px 28px;
  }
  .contact-list {
    list-style: none;
    color: var(--ink-white);
    font-size: 14.5px;
    letter-spacing: 0.5px;
  }
  .contact-list li { display: flex; line-height: 26px; }
  .contact-list__key {
    width: 24px;
    border-right: 1px solid var(--ink-white);
    margin-right: 10px;
  }

  /* Back */
  .back-brand {
    position: absolute;
    top: 230px;
    left: 170px;
    transform: translate(-50%, -50%) rotate(90deg);
    white-space: nowrap;
    display: flex;
    flex-direction: column-reverse;
  }
  .back-brand__name {
    color: var(--orange);
    font-size: 50px;
    line-height: 1;
  }
  .back-brand__tagline {
    color: var(--ink-white);
    font-size: 15px;
    margin-bottom: 6px;
    text-align: right;
  }
  .address-band {
    position: absolute;
    left: 0;
    right: 0;
    bottom: 0;
    height: 120px;
    background: var(--card-white);
    display: flex;
    align-items: center;
    justify-content: center;
    text-align: center;
  }
  .address {
    font-style: normal;
    color: var(--orange);
    font-size: 16px;
    line-height: 1.45;
  }
</style>
</head>
<body>
  <section class="card card--front" aria-label="Business card front">
    <div class="brand">
      <span class="brand__name">Tovimerra</span>
      <span class="brand__tagline">drift into calm</span>
    </div>
    <div class="person">
      <p class="person__name">Dana Whitlow</p>
      <p class="person__title">Managing Director</p>
    </div>
    <div class="contact-band">
      <ul class="contact-list">
        <li><span class="contact-list__key">O</span><span>800.46.TOVI (868400)</span></li>
        <li><span class="contact-list__key">M</span><span>555.201.0148</span></li>
        <li><span class="contact-list__key">F</span><span>555.304.0172</span></li>
        <li><span class="contact-list__key">W</span><span>tovimerra.com</span></li>
      </ul>
    </div>
  </section>

  <section class="card card--back" aria-label="Business card back">
    <div class="back-brand">
      <span class="back-brand__name">Tovimerra</span>
      <span class="back-brand__tagline">drift into calm</span>
    </div>
    <div class="address-band">
      <address class="address">1640 Marlowe Bay Road,<br>Port Ellery, 90411</address>
    </div>
  </section>
</body>
</html>
```